carpet cleaning flyer/leaflet modern/upmarket twist

We are Velvet Nest, We do carpet & upholstery cleaning for the domestic market, if you are able to incorporate images like the ones I have provided that would be awesome, please feel free to find similar! mine are only examples. id like a front cover photo with the company name running through it, and the back to be half picture and then the detailing of what we do which is in the document I've uploaded
Target Market(s)
Domestic house hold
Industry/Entity Type
Cleaning Service
Colors
eea4c8
e667a6
c3c3c3
cbcbcb
aaaaaa
f59296
Requirements
Must have
- It must be 2 sided also have A modern but upmarket feel, a luxury. a front picture with name on it, back page with picture and writing from the word document.
Nice to have
- a input from yourselves, your twist on it

```html
<!DOCTYPE html>
<html lang="en">
<head>
<meta charset="utf-8">
<title>Velvet Nest – Flyer Concept</title>
<link href="https://fonts.googleapis.com/css2?family=Open+Sans:wght@300;400;600;700&family=Jost:wght@300&display=swap" rel="stylesheet">
<style>
  :root {
    --pink: #f03f80;
    --blue: #0a6fcc;
    --charcoal: #262626;
    --black: #050505;
    --white: #ffffff;
    --floor: #dcdcdc;
    --label: #1a1a1a;
    --room-light: #c9cfc4;
    --room-mid: #9c9a9e;
    --carpet-grey: #6b6b6b;
    --carpet-dark: #4a4a4a;
    --carpet-beige: #c2a882;
    --carpet-brown: #6e5a45;
    --carpet-white: #efecec;
    --wine-tint: #e3c3c9;
  }
  * { box-sizing: border-box; margin: 0; padding: 0; }
  html, body { width: 1200px; height: 1000px; overflow: hidden; }
  body {
    position: relative;
    font-family: "Open Sans", Arial, sans-serif;
    background: linear-gradient(to bottom, var(--white) 0, var(--white) 677px, var(--floor) 677px, #f6f6f6 960px, var(--white) 1000px);
  }
  .sheet { position: absolute; overflow: hidden; }
  .sheet--front { left: 115px; top: 87px; width: 465px; height: 658px; }
  .sheet--back { left: 664px; top: 85px; width: 466px; height: 660px; background: var(--white); }

  .photo { position: absolute; }
  .photo--lounge {
    inset: 0;
    background: linear-gradient(to bottom, var(--room-light) 0, #b4b3b6 30%, var(--room-mid) 48%, var(--carpet-grey) 72%, var(--carpet-dark) 100%);
  }
  .photo--spill {
    left: 0; top: 0; width: 263px; height: 367px;
    background: linear-gradient(to bottom, var(--carpet-brown) 0, #9a8163 22%, var(--carpet-beige) 45%, #b89c76 75%, #9c7d55 100%);
  }
  .photo--wine {
    left: 266px; top: 0; width: 200px; height: 272px;
    background: linear-gradient(to bottom, var(--carpet-white) 0, #f3f1f1 45%, var(--wine-tint) 100%);
  }

  .title { position: absolute; left: 28px; font-weight: 700; font-size: 58px; line-height: 67px; color: var(--pink); padding: 0 14px; letter-spacing: 1px; }
  .title--dark { top: 366px; background: var(--black); }
  .title--light { top: 440px; background: var(--white); }
  .tagline { position: absolute; left: 27px; top: 516px; color: var(--white); font-weight: 300; font-size: 32px; line-height: 38px; }

  .contact-bar {
    position: absolute; left: 0; bottom: 0; width: 100%; height: 36px;
    display: flex; align-items: center; gap: 14px; padding-left: 26px;
    color: var(--white); font-size: 15px; font-weight: 600;
  }
  .contact-bar--pink { background: var(--pink); }
  .contact-bar--black { background: var(--black); }
  .contact-item { display: flex; align-items: center; gap: 6px; }
  .contact-item--email { font-weight: 400; }
  .contact-item svg { flex: none; }

  .feature { position: absolute; color: var(--white); padding: 14px 10px 14px 15px; }
  .feature--professional { left: 0; top: 367px; width: 263px; height: 147px; background: var(--pink); }
  .feature--reliable { left: 266px; top: 272px; width: 200px; height: 242px; background: var(--blue); padding-top: 17px; }
  .feature--trustworthy { left: 0; top: 516px; width: 466px; height: 108px; background: var(--charcoal); }
  .feature-heading { display: flex; align-items: center; gap: 10px; font-size: 22px; font-weight: 700; margin-bottom: 8px; letter-spacing: 0.3px; }
  .feature-text { font-size: 12.4px; line-height: 15px; letter-spacing: -0.1px; }
  .feature-text + .feature-text { margin-top: 15px; }

  .board-label { position: absolute; top: 770px; font-size: 22px; color: var(--label); transform: translateX(-50%); }
  .board-label--front { left: 347px; }
  .board-label--back { left: 896px; }
  .board-title { position: absolute; left: 617px; top: 840px; transform: translateX(-50%); font-family: "Jost", Arial, sans-serif; font-weight: 300; font-size: 40px; color: var(--label); }
</style>
</head>
<body>
  <section class="sheet sheet--front">
    <div class="photo photo--lounge" role="img" aria-label="Grey armchair with pink and patterned cushions on a soft grey carpet by a sunny window"></div>
    <h1 class="title title--dark">VELVET</h1>
    <div class="title title--light">NEST</div>
    <p class="tagline">Carpet and<br>Upholstery Cleaning</p>
    <footer class="contact-bar contact-bar--pink">
      <span class="contact-item">
        <svg width="16" height="16" viewBox="0 0 24 24"><path fill="#fff" d="M6.6 10.8c1.4 2.8 3.8 5.1 6.6 6.6l2.2-2.2c.3-.3.7-.4 1-.2 1.1.4 2.3.6 3.6.6.6 0 1 .4 1 1V20c0 .6-.4 1-1 1C10.6 21 3 13.4 3 4c0-.6.4-1 1-1h3.5c.6 0 1 .4 1 1 0 1.3.2 2.5.6 3.6.1.3 0 .7-.2 1z"/></svg>
        01632 960 418
      </span>
      <span class="contact-item contact-item--email">
        <svg width="17" height="12" viewBox="0 0 17 12"><rect x="0.75" y="0.75" width="15.5" height="10.5" fill="none" stroke="#fff" stroke-width="1.2"/><path d="M1 1l7.5 6L16 1" fill="none" stroke="#fff" stroke-width="1.2"/></svg>
        sam.reed@velvetnest.co.uk
      </span>
    </footer>
  </section>

  <section class="sheet sheet--back">
    <div class="photo photo--spill" role="img" aria-label="Tipped-over white mug spilling coffee onto a beige carpet"></div>
    <div class="photo photo--wine" role="img" aria-label="Fallen wine glass with red wine stain on a white carpet"></div>

    <article class="feature feature--professional">
      <h2 class="feature-heading">
        <svg width="24" height="24" viewBox="0 0 24 24"><circle cx="12" cy="12" r="11" fill="#fff"/><path d="M7 12.5l3.3 3.2L17 9" fill="none" stroke="var(--pink)" stroke-width="2.6" stroke-linecap="round" stroke-linejoin="round"/></svg>
        PROFESSIONAL
      </h2>
      <p class="feature-text">We use the latest hot water extraction cleaning technology to give us the ability to get into the ground down dirt deep down inside the Fibres.</p>
    </article>

    <article class="feature feature--reliable">
      <h2 class="feature-heading">
        <svg width="24" height="24" viewBox="0 0 24 24"><circle cx="12" cy="12" r="11" fill="#fff"/><path d="M7 12.5l3.3 3.2L17 9" fill="none" stroke="var(--blue)" stroke-width="2.6" stroke-linecap="round" stroke-linejoin="round"/></svg>
        RELIABLE
      </h2>
      <p class="feature-text">We pride ourselves on providing outstanding services to our customers.</p>
      <p class="feature-text">From a single carpet or rug, to a whole-house clean, we provide a reliable and friend-ly service. Call us to discuss your needs.</p>
    </article>

    <article class="feature feature--trustworthy">
      <h2 class="feature-heading">
        <svg width="24" height="24" viewBox="0 0 24 24"><circle cx="12" cy="12" r="11" fill="#fff"/><path d="M7 12.5l3.3 3.2L17 9" fill="none" stroke="var(--charcoal)" stroke-width="2.6" stroke-linecap="round" stroke-linejoin="round"/></svg>
        TRUSTWORTHY
      </h2>
      <p class="feature-text">We are fully insured to work in your home, we guarantee all our work so if any issues do arise we will do our up most to put it back right for you.</p>
    </article>

    <footer class="contact-bar contact-bar--black">
      <span class="contact-item">
        <svg width="16" height="16" viewBox="0 0 24 24"><path fill="#fff" d="M6.6 10.8c1.4 2.8 3.8 5.1 6.6 6.6l2.2-2.2c.3-.3.7-.4 1-.2 1.1.4 2.3.6 3.6.6.6 0 1 .4 1 1V20c0 .6-.4 1-1 1C10.6 21 3 13.4 3 4c0-.6.4-1 1-1h3.5c.6 0 1 .4 1 1 0 1.3.2 2.5.6 3.6.1.3 0 .7-.2 1z"/></svg>
        01632 960 418
      </span>
      <span class="contact-item contact-item--email">
        <svg width="17" height="12" viewBox="0 0 17 12"><rect x="0.75" y="0.75" width="15.5" height="10.5" fill="none" stroke="#fff" stroke-width="1.2"/><path d="M1 1l7.5 6L16 1" fill="none" stroke="#fff" stroke-width="1.2"/></svg>
        sam.reed@velvetnest.co.uk
      </span>
    </footer>
  </section>

  <p class="board-label board-label--front">FRONT</p>
  <p class="board-label board-label--back">BACK</p>
  <p class="board-title">Concept1</p>
</body>
</html>
```